Design trifold flyer for patients

Hi buddy,I need a trifold brochure for an early event that month. I just need a design template in Adobe Illustrator, so that I can modify it later.Size: A4 divide into 3 pages, 10x21cm each. The total has 6 page with both sides.Content: (Page)1. Cover with logo, address, phone number, etc..2. Instruction: An image and a paragraph3 + 4. A content list, paragraph5. Note with patients6. Price listColor: blue and light blue, greenTarget audience: Patients

Target Market(s)

Patients in hospital

Industry/Entity Type

Medical

Font styles to use
Sans Serif

Colors
85cae6
33b8a4
0692cd

Requirements
Must have
• picture place holder
Nice to have
• icon

```html
<!DOCTYPE html>
<html lang="en">
<head>
<meta charset="utf-8">
<title>Hanbit Medical Center – Patient Trifold</title>
<link href="https://fonts.googleapis.com/css2?family=Open+Sans:wght@400;600;700&display=swap" rel="stylesheet">
<style>
  :root{
    --blue:#0692cd;
    --navy:#1d4fa3;
    --light:#85cae6;
    --pale:#dff1f8;
    --ice:#eef8fc;
    --dark:#2b2d31;
    --ink:#333a44;
    --paper:#ffffff;
    --stage:#e4e4e4;
  }
  *{box-sizing:border-box;margin:0;padding:0}
  html,body{width:900px;height:1200px;overflow:hidden;background:var(--stage);font-family:"Open Sans",Arial,sans-serif;color:var(--ink)}
  .sheet{position:absolute;left:50px;width:800px;height:566px;background:var(--paper);box-shadow:0 4px 14px rgba(0,0,0,.18);overflow:hidden}
  .sheet--outside{top:22px}
  .sheet--inside{top:612px}
  .sheet svg.art{position:absolute;inset:0;width:800px;height:566px}
  .fold{position:absolute;top:0;bottom:0;width:1px;background:rgba(0,0,0,.06)}
  .brand{position:absolute;font-weight:700;color:var(--navy);letter-spacing:.5px;display:flex;align-items:center;gap:6px}
  .brand__mark{width:12px;height:12px;background:var(--blue)}
  .brand__sub{position:absolute;font-size:8px;font-weight:600;color:var(--navy);text-transform:uppercase;line-height:1.25}
  .url{position:absolute;font-size:10px;font-weight:700;color:var(--dark)}
  .contact{position:absolute;left:267px;width:266px;top:120px;text-align:center;font-size:10px;line-height:1.4;color:var(--dark)}
  .contact__item{margin-bottom:12px;display:flex;flex-direction:column;align-items:center;gap:4px}
  .contact__item svg{width:12px;height:12px}
  .tagline{position:absolute;left:690px;top:262px;width:100px;text-align:right;color:#fff;font-size:13px;line-height:1.2}
  .block{position:absolute;width:230px}
  .block__title{display:flex;align-items:center;gap:8px;font-size:12px;font-weight:700;color:var(--blue);margin-bottom:6px}
  .block__icon{width:20px;height:20px;border:1.5px solid #9aa6b2;border-radius:50%;display:flex;align-items:center;justify-content:center}
  .block__icon svg{width:11px;height:11px}
  .block__text{font-size:9px;line-height:1.35;color:var(--ink);text-align:justify}
  .checklist{position:absolute;left:28px;top:392px;width:220px;color:#fff}
  .checklist .block__title{color:#fff;margin-bottom:8px}
  .checklist ul{list-style:none;font-size:9.5px;line-height:1.5}
  .checklist li::before{content:"";display:inline-block;width:5px;height:5px;background:var(--blue);margin-right:7px;vertical-align:middle}
  .side-url{position:absolute;left:768px;top:150px;width:20px;height:300px;writing-mode:vertical-rl;color:#fff;font-size:11px;font-weight:600;letter-spacing:.5px}
</style>
</head>
<body>

<section class="sheet sheet--outside" aria-label="Brochure outside">
  <svg class="art" viewBox="0 0 800 566">
    <defs>
      <linearGradient id="paleWash" x1="0" y1="0" x2="0" y2="1">
        <stop offset="0" stop-color="#e9f6fb"/><stop offset="1" stop-color="#bfe3f1"/>
      </linearGradient>
      <linearGradient id="coatTone" x1="0" y1="0" x2="1" y2="1">
        <stop offset="0" stop-color="#f4f6f8"/><stop offset="1" stop-color="#d5dbe0"/>
      </linearGradient>
      <linearGradient id="techTone" x1="0" y1="0" x2="1" y2="1">
        <stop offset="0" stop-color="#07163a"/><stop offset="1" stop-color="#1b4a8a"/>
      </linearGradient>
      <linearGradient id="doctorTone" x1="0" y1="0" x2="1" y2="0">
        <stop offset="0" stop-color="#e6f3f7"/><stop offset="1" stop-color="#9fd6e7"/>
      </linearGradient>
    </defs>
    <rect width="800" height="566" fill="url(#paleWash)"/>

    <g role="img" aria-label="Photo of a white doctor's coat with a stethoscope">
      <path d="M0 0H267V300L0 370Z" fill="url(#coatTone)"/>
    </g>
    <path d="M0 380L267 312V322L0 392Z" fill="var(--blue)"/>
    <path d="M0 400L267 332V372L0 442Z" fill="var(--light)"/>
    <path d="M0 470L150 448L0 505Z" fill="var(--dark)"/>
    <path d="M0 556H267V566H0Z" fill="var(--navy)"/>

    <path d="M267 312L533 250V262L267 324Z" fill="var(--blue)"/>
    <path d="M267 332L533 270V320L267 372Z" fill="var(--light)"/>
    <g role="img" aria-label="Digital illustration of glowing medical technology on dark blue">
      <path d="M300 372L533 320V566H300Z" fill="url(#techTone)"/>
    </g>
    <path d="M267 556H533V566H267Z" fill="var(--navy)"/>

    <g role="img" aria-label="Photo of a doctor using a digital touch screen">
      <rect x="533" y="0" width="267" height="200" fill="url(#doctorTone)"/>
    </g>
    <path d="M533 200H800V245L533 262Z" fill="var(--light)"/>
    <path d="M600 280L800 238V330Z" fill="var(--dark)"/>
    <path d="M533 556H800V566H533Z" fill="var(--navy)"/>
  </svg>
  <div class="fold" style="left:267px"></div>
  <div class="fold" style="left:533px"></div>

  <div class="brand" style="left:40px;top:262px;font-size:28px"><span class="brand__mark"></span>HANBIT</div>
  <div class="brand" style="left:58px;top:302px;font-size:15px">한빛메디컬센터</div>
  <div class="url" style="left:150px;top:528px">www.hanbitmc.org</div>

  <div class="brand" style="left:340px;top:40px;font-size:20px"><span class="brand__mark"></span>HANBIT</div>
  <div class="brand__sub" style="left:358px;top:70px;width:140px">Hanbit Medical<br>Center</div>
  <div class="contact">
    <div class="contact__item">
      <svg viewBox="0 0 12 12"><path d="M6 1a3.5 3.5 0 0 0-3.5 3.5C2.5 7.5 6 11 6 11s3.5-3.5 3.5-6.5A3.5 3.5 0 0 0 6 1z" fill="none" stroke="#2b2d31"/><circle cx="6" cy="4.5" r="1.2" fill="#2b2d31"/></svg>
      <span>48, CHEONGNA-RO SEO-GU,<br>INCHEON 22740, Rep. of KOREA</span>
    </div>
    <div class="contact__item">
      <svg viewBox="0 0 12 12"><path d="M3 1.5l2 2-1 1.5a6 6 0 0 0 3 3l1.5-1 2 2-1.5 1.5C5.5 10.5 1.5 6.5 1.5 3z" fill="none" stroke="#2b2d31"/></svg>
      <span>82-2-555-0147</span>
    </div>
    <div class="contact__item">
      <svg viewBox="0 0 12 12"><circle cx="6" cy="6" r="4.8" fill="none" stroke="#2b2d31"/><path d="M1.2 6h9.6M6 1.2c-2 2.6-2 7 0 9.6M6 1.2c2 2.6 2 7 0 9.6" fill="none" stroke="#2b2d31" stroke-width=".8"/></svg>
      <span>www.hanbitmc.org</span>
    </div>
  </div>

  <div class="tagline">Lorem ipsum<br>dolor sit<br>amet</div>
  <div class="brand" style="left:570px;top:395px;font-size:18px"><span class="brand__mark"></span>HANBIT</div>
  <div class="brand__sub" style="left:680px;top:398px;width:110px">Hanbit Medical<br>Center</div>
  <div class="url" style="left:690px;top:528px">www.hanbitmc.org</div>
</section>

<section class="sheet sheet--inside" aria-label="Brochure inside">
  <svg class="art" viewBox="0 0 800 566">
    <defs>
      <linearGradient id="dnaTone" x1="0" y1="0" x2="1" y2="0">
        <stop offset="0" stop-color="#cfe9f6"/><stop offset=".5" stop-color="#3aa6e0"/><stop offset="1" stop-color="#0b5fb4"/>
      </linearGradient>
      <linearGradient id="careTone" x1="0" y1="0" x2="1" y2="1">
        <stop offset="0" stop-color="#eef2f5"/><stop offset="1" stop-color="#b9c9d6"/>
      </linearGradient>
    </defs>
    <rect width="800" height="566" fill="#fff"/>
    <rect x="533" width="267" height="566" fill="#f3f4f6"/>

    <g role="img" aria-label="Banner illustration of a blue DNA helix">
      <path d="M267 0H760V55C640 30 450 70 267 90Z" fill="url(#dnaTone)"/>
    </g>
    <rect x="760" y="0" width="40" height="566" fill="var(--dark)"/>
    <path d="M620 566L740 530L760 566Z" fill="var(--navy)"/>
    <path d="M267 545C420 535 560 540 760 520V566H267Z" fill="var(--blue)"/>

    <g role="img" aria-label="Photo of a doctor holding a patient's hands">
      <polygon points="60,185 110,155 160,185 160,245 110,275 60,245" fill="url(#careTone)" stroke="var(--light)" stroke-width="2"/>
    </g>
    <g role="img" aria-label="Photo of a doctor examining a pregnant patient">
      <polygon points="168,255 200,236 232,255 232,295 200,314 168,295" fill="url(#careTone)" stroke="var(--light)" stroke-width="2"/>
    </g>
    <path d="M20 375L250 355V545H20Z" fill="var(--dark)"/>

    <g role="img" aria-label="Photo of medical staff at a patient's bedside">
      <polygon points="330,250 400,210 470,250 470,330 400,370 330,330" fill="url(#careTone)" stroke="var(--light)" stroke-width="2"/>
    </g>
    <g role="img" aria-label="Photo of a nurse caring for an elderly patient">
      <polygon points="305,420 345,397 385,420 385,466 345,489 305,466" fill="url(#careTone)" stroke="var(--light)" stroke-width="2"/>
    </g>
    <g role="img" aria-label="Photo of a surgeon in an operating room">
      <polygon points="415,410 455,387 495,410 495,456 455,479 415,456" fill="url(#careTone)" stroke="var(--light)" stroke-width="2"/>
    </g>
  </svg>
  <div class="fold" style="left:267px"></div>
  <div class="fold" style="left:533px"></div>

  <div class="block" style="left:20px;top:30px">
    <div class="block__title"><span class="block__icon"><svg viewBox="0 0 12 12"><path d="M6 2v8M2 6h8" stroke="#666" stroke-width="1.6"/></svg></span>Lorem ipsum</div>
    <p class="block__text">Lorem ipsum dolor sit amet, consectetur adipiscing elit, sed do eiusmod tempor incididunt ut labore et dolore magna aliqua. Ut enim ad minim veniam, quis nostrud exercitation ullamco laboris nisi ut aliquip ex ea commodo consequat.</p>
  </div>

  <div class="checklist">
    <div class="block__title"><span class="block__icon" style="border-color:#fff"><svg viewBox="0 0 12 12"><path d="M2 6.5l2.5 2.5L10 3" fill="none" stroke="#fff" stroke-width="1.6"/></svg></span>Lorem ipsum</div>
    <ul>
      <li>Lorem ipsum dolor sit amet</li>
      <li>Consectetur adipiscing elit</li>
      <li>Sed do eiusmod tempor incididunt</li>
      <li>Labore et dolore magna aliqua</li>
      <li>Ut enim ad minim veniam</li>
      <li>Quis nostrud exercitation ullamco</li>
      <li>Laboris nisi ut aliquip ex ea</li>
    </ul>
  </div>

  <div class="block" style="left:285px;top:100px">
    <div class="block__title"><span class="block__icon"><svg viewBox="0 0 12 12"><rect x="2" y="3" width="8" height="7" fill="none" stroke="#666" stroke-width="1.3"/><path d="M4 3V1.5h4V3" fill="none" stroke="#666"/></svg></span>Lorem ipsum</div>
    <p class="block__text">Lorem ipsum dolor sit amet, consectetur adipiscing elit, sed do eiusmod tempor incididunt ut labore et dolore magna aliqua. Ut enim ad minim veniam, quis nostrud exercitation ullamco laboris nisi ut aliquip ex ea commodo consequat.</p>
  </div>

  <div class="block" style="left:548px;top:100px;width:200px">
    <div class="block__title"><span class="block__icon"><svg viewBox="0 0 12 12"><path d="M6 10S1.5 7 1.5 4.2A2.2 2.2 0 0 1 6 3a2.2 2.2 0 0 1 4.5 1.2C10.5 7 6 10 6 10z" fill="none" stroke="#666" stroke-width="1.2"/></svg></span>Lorem ipsum</div>
    <p class="block__text">Lorem ipsum dolor sit amet, consectetur adipiscing elit, sed do eiusmod tempor incididunt ut labore et dolore magna aliqua. Ut enim ad minim veniam, quis nostrud exercitation ullamco laboris nisi ut aliquip ex ea commodo consequat.</p>
  </div>
  <div class="block" style="left:548px;top:230px;width:200px">
    <div class="block__title"><span class="block__icon"><svg viewBox="0 0 12 12"><path d="M6 2v8M2 6h8" stroke="#666" stroke-width="1.6"/></svg></span>Lorem ipsum</div>
    <p class="block__text">Lorem ipsum dolor sit amet, consectetur adipiscing elit, sed do eiusmod tempor incididunt ut labore et dolore magna aliqua. Ut enim ad minim veniam, quis nostrud exercitation ullamco laboris nisi ut aliquip ex ea commodo consequat.</p>
  </div>
  <div class="block" style="left:548px;top:360px;width:200px">
    <div class="block__title"><span class="block__icon"><svg viewBox="0 0 12 12"><rect x="2" y="3" width="8" height="7" fill="none" stroke="#666" stroke-width="1.3"/><path d="M4 3V1.5h4V3" fill="none" stroke="#666"/></svg></span>Lorem ipsum</div>
    <p class="block__text">Lorem ipsum dolor sit amet, consectetur adipiscing elit, sed do eiusmod tempor incididunt ut labore et dolore magna aliqua. Ut enim ad minim veniam, quis nostrud exercitation ullamco laboris nisi ut aliquip ex ea commodo consequat.</p>
  </div>

  <div class="side-url">www.hanbitmc.org/global/en/main</div>
</section>

</body>
</html>
```